social interest sharing site needs a web site design

we need a web site design for a social web platform.
the site is one page(main page), that is split into 3 sections
each section is a different color(red,green and blue)
and a user can choose to share each of the sections.
any section/color will contain boxes , each box can contain different media types.

the media types:
* list of URLS
* list of articles including title + image + description
* list of videos
* thumbnails of images
* calender
* list of emails

the main content will look like corkboardly layout
multiple boxes each box can contain different type of content as described above

each color is a different tab
each tab will have layout like corkboardly
Updates

please read the last description update.
and i uploaded an image that can explain the requirements better

thanks
Oren
 

Industry/Entity Type

Media

```html
<!DOCTYPE html>
<html lang="en">
<head>
<meta charset="utf-8">
<title>Quillo.me – Home</title>
<link rel="stylesheet" href="https://fonts.googleapis.com/css2?family=Fredoka+One&family=Open+Sans:wght@400;600;700&display=swap">
<style>
:root{
  --ink:#2b2d31;
  --bar:#34363b;
  --band:#e9e9ea;
  --coral:#f7837b;
  --coral-deep:#f26d64;
  --teal:#35c7a6;
  --sky:#29a9e0;
  --card:#ffffff;
  --rail:#f3f3f3;
  --text:#3b3b3b;
  --muted:#8a8a8a;
  --icon:#4a4a4a;
  --pill:#dcdcdc;
}
*{box-sizing:border-box;margin:0;padding:0}
html,body{width:1200px;height:3044px;overflow:hidden}
body{font-family:"Open Sans",Arial,sans-serif;color:var(--text);background:var(--coral)}

.topbar{height:76px;background:var(--bar);position:relative}
.brand{position:absolute;left:26px;top:10px;font-family:"Fredoka One","Open Sans",sans-serif;font-size:50px;line-height:56px;color:var(--coral)}
.search{position:absolute;left:600px;top:26px;width:212px;height:30px;border-bottom:1px solid #55585e;color:#b9bbbf;font-size:13px;line-height:26px}
.search svg{position:absolute;right:4px;top:6px}
.social{position:absolute;top:19px;width:40px;height:40px;border-radius:3px}
.social.one{left:845px;background:var(--coral-deep)}
.social.two{left:890px;background:var(--teal)}
.social.help{left:936px;background:var(--sky);color:#fff;font-weight:700;font-size:26px;text-align:center;line-height:40px}
.btn{position:absolute;top:23px;height:34px;border-radius:3px;color:#fff;font-weight:700;font-size:13px;line-height:34px;text-align:center}
.btn.login{left:1014px;width:76px;background:#5b5e64}
.btn.signup{left:1096px;width:76px;background:var(--coral-deep)}

.subnav{height:102px;background:var(--band);position:relative}
.tab{position:absolute;top:25px;height:66px;padding:12px 16px;color:#fff;font-weight:700;text-transform:uppercase;line-height:1.05}
.tab small{display:block;font-size:13px;font-weight:600}
.tab span{font-size:20px}
.tab.home{left:28px;width:162px;background:var(--coral)}
.tab.videos{left:200px;width:220px;background:var(--teal)}
.tab.apps{left:426px;width:208px;background:var(--sky)}
.following{position:absolute;left:677px;top:44px;font-size:13px;font-weight:700;color:var(--ink);line-height:1.2}
.pill{position:absolute;top:40px;height:46px;padding:7px 10px;background:var(--pill);font-size:11.5px;line-height:15px;color:var(--ink)}
.pill.a{left:774px;width:114px}
.pill.b{left:900px;width:114px}
.pill.c{left:1026px;width:146px}

.board{position:absolute;top:203px;left:28px;display:grid;grid-template-columns:repeat(3,358px);column-gap:35px;row-gap:38px}
.card{width:358px;height:350px;background:var(--card);box-shadow:0 2px 4px rgba(0,0,0,.18);display:flex;flex-direction:column}
.media{height:233px;width:100%}
.info{flex:1;display:flex}
.body{flex:1;padding:12px 10px 0 10px}
.title{display:flex;align-items:center;font-size:14.5px;font-weight:600;color:var(--ink);margin-bottom:10px}
.mark{width:18px;height:18px;border-radius:2px;margin-right:8px;flex:none}
.mark.post{background:#3f5d9b}
.mark.tweet{background:#2fb3e8}
.mark.clip{background:#d9322b}
.desc{font-size:11.5px;line-height:17px;color:var(--muted)}
.rail{width:32px;background:var(--rail);display:flex;flex-direction:column;align-items:center;justify-content:space-around;padding:6px 0}
.rail svg{width:15px;height:15px;fill:var(--icon)}

.video{background:#050505;position:relative}
.video .play{position:absolute;left:134px;top:66px}
.video .controls{position:absolute;left:8px;right:8px;bottom:10px;height:8px;display:flex;align-items:center;gap:6px}
.controls i{display:block;height:3px;background:#6a6a6a;border-radius:2px}
.controls .track{flex:1}
.controls .dot{width:8px;height:8px;background:#9a9a9a}
.controls .vol{width:26px}

.seal{position:absolute;left:575px;top:2918px;width:50px;height:50px;border-radius:50%;background:#fff;box-shadow:0 1px 3px rgba(0,0,0,.2)}
.seal::after{content:"";position:absolute;left:17px;top:17px;width:16px;height:16px;border-radius:50%;background:#f5a623}
.footer{position:absolute;left:0;top:2994px;width:1200px;height:50px;background:var(--bar);color:#9a9ca0;font-size:12px;text-align:center;line-height:50px}
</style>
</head>
<body>
<svg width="0" height="0" style="position:absolute">
  <symbol id="i-eye" viewBox="0 0 24 24"><path d="M12 5C6 5 2 12 2 12s4 7 10 7 10-7 10-7-4-7-10-7zm0 11a4 4 0 1 1 0-8 4 4 0 0 1 0 8zm0-6a2 2 0 1 0 0 4 2 2 0 0 0 0-4z"/></symbol>
  <symbol id="i-star" viewBox="0 0 24 24"><path d="M12 2l3 7 7 .6-5.3 4.6 1.6 7.3L12 17.8 5.7 21.5l1.6-7.3L2 9.6 9 9z" fill="none" stroke="#4a4a4a" stroke-width="2"/></symbol>
  <symbol id="i-heart" viewBox="0 0 24 24"><path d="M12 21l-8.5-8.3A5.3 5.3 0 0 1 12 5.5a5.3 5.3 0 0 1 8.5 7.2z"/></symbol>
  <symbol id="i-cloud" viewBox="0 0 24 24"><path d="M18 10a6 6 0 0 0-11.6-1.5A4.5 4.5 0 0 0 6.5 19H18a4.5 4.5 0 0 0 0-9zm-6 8l-4-4h3v-4h2v4h3z"/></symbol>
</svg>

<header class="topbar">
  <div class="brand">Quillo.me</div>
  <div class="search">Search here
    <svg width="14" height="14" viewBox="0 0 24 24"><circle cx="10" cy="10" r="7" fill="none" stroke="#8c8f94" stroke-width="2.5"/><path d="M15 15l6 6" stroke="#8c8f94" stroke-width="2.5"/></svg>
  </div>
  <div class="social one"></div>
  <div class="social two"></div>
  <div class="social help">?</div>
  <div class="btn login">LOG IN</div>
  <div class="btn signup">SIGN UP</div>
</header>

<nav class="subnav">
  <div class="tab home"><small>My</small><span>Home Page</span></div>
  <div class="tab videos"><small>My</small><span>Favorites Videos</span></div>
  <div class="tab apps"><small>My</small><span>Personal Apps</span></div>
  <div class="following">Following<br>QUILLO</div>
  <div class="pill a">Marens Favorites Videos</div>
  <div class="pill b">Talis Pics + Favorites Link</div>
  <div class="pill c">Family Weekly Calender and notes</div>
</nav>

<main class="board">
  <!-- row 1 -->
  <article class="card"><div class="media" role="img" aria-label="Living room decorated with a Christmas tree and fireplace" style="background:linear-gradient(135deg,#6b3a1f,#c7843f 60%,#8a2c1f)"></div>
    <div class="info"><div class="body"><div class="title"><span class="mark post"></span>Lorem Ipsum is simply dummy</div><p class="desc">Lorem Ipsum is simply dummy text of the printing and typesetting industry. Lorem Ipsum has been the industry's standard dummy text ever since.</p></div>
    <div class="rail"><svg><use href="#i-eye"/></svg><svg><use href="#i-star"/></svg><svg><use href="#i-heart"/></svg><svg><use href="#i-cloud"/></svg></div></div></article>
  <article class="card"><div class="media" role="img" aria-label="Group of friends in holiday hats by a Christmas tree" style="background:linear-gradient(135deg,#2f6b3a,#e8e2dc 55%,#d23a3a)"></div>
    <div class="info"><div class="body"><div class="title"><span class="mark tweet"></span>Lorem Ipsum is simply dummy</div><p class="desc">Lorem Ipsum is simply dummy text of the printing and typesetting industry. Lorem Ipsum has been the industry's standard dummy text ever since.</p></div>
    <div class="rail"><svg><use href="#i-eye"/></svg><svg><use href="#i-star"/></svg><svg><use href="#i-heart"/></svg><svg><use href="#i-cloud"/></svg></div></div></article>
  <article class="card"><div class="media video" role="img" aria-label="Video player">
      <svg class="play" width="90" height="90" viewBox="0 0 90 90"><circle cx="45" cy="45" r="41" fill="none" stroke="#fff" stroke-width="5"/><path d="M36 28v34l27-17z" fill="#fff"/></svg>
      <div class="controls"><i class="dot"></i><i class="track"></i><i class="vol"></i></div></div>
    <div class="info"><div class="body"><div class="title"><span class="mark clip"></span>Lorem Ipsum is simply dummy</div><p class="desc">Lorem Ipsum is simply dummy text of the printing and typesetting industry. Lorem Ipsum has been the industry's standard dummy text ever since.</p></div>
    <div class="rail"><svg><use href="#i-eye"/></svg><svg><use href="#i-star"/></svg><svg><use href="#i-heart"/></svg><svg><use href="#i-cloud"/></svg></div></div></article>

  <!-- row 2 -->
  <article class="card"><div class="media" role="img" aria-label="Family playing outdoors in the snow" style="background:linear-gradient(160deg,#1f63b3,#8fb9e0 60%,#e9eef5)"></div>
    <div class="info"><div class="body"><div class="title"><span class="mark post"></span>Lorem Ipsum is simply dummy</div><p class="desc">Lorem Ipsum is simply dummy text of the printing and typesetting industry. Lorem Ipsum has been the industry's standard dummy text ever since.</p></div>
    <div class="rail"><svg><use href="#i-eye"/></svg><svg><use href="#i-star"/></svg><svg><use href="#i-heart"/></svg><svg><use href="#i-cloud"/></svg></div></div></article>
  <article class="card"><div class="media" role="img" aria-label="Couple looking at a laptop together" style="background:linear-gradient(135deg,#f2ece6,#c98e6c 55%,#5a6f8f)"></div>
    <div class="info"><div class="body"><div class="title"><span class="mark tweet"></span>Lorem Ipsum is simply dummy</div><p class="desc">Lorem Ipsum is simply dummy text of the printing and typesetting industry. Lorem Ipsum has been the industry's standard dummy text ever since.</p></div>
    <div class="rail"><svg><use href="#i-eye"/></svg><svg><use href="#i-star"/></svg><svg><use href="#i-heart"/></svg><svg><use href="#i-cloud"/></svg></div></div></article>
  <article class="card"><div class="media" role="img" aria-label="Family having a picnic on the grass" style="background:linear-gradient(180deg,#8fb84a,#d9a24a 55%,#5d9a2c)"></div>
    <div class="info"><div class="body"><div class="title"><span class="mark clip"></span>Lorem Ipsum is simply dummy</div><p class="desc">Lorem Ipsum is simply dummy text of the printing and typesetting industry. Lorem Ipsum has been the industry's standard dummy text ever since.</p></div>
    <div class="rail"><svg><use href="#i-eye"/></svg><svg><use href="#i-star"/></svg><svg><use href="#i-heart"/></svg><svg><use href="#i-cloud"/></svg></div></div></article>

  <!-- row 3 -->
  <article class="card"><div class="media" role="img" aria-label="Glasses of green smoothie with apples" style="background:linear-gradient(135deg,#c9e07a,#5f9a2a 55%,#eef4e0)"></div>
    <div class="info"><div class="body"><div class="title"><span class="mark post"></span>Lorem Ipsum is simply dummy</div><p class="desc">Lorem Ipsum is simply dummy text of the printing and typesetting industry. Lorem Ipsum has been the industry's standard dummy text ever since.</p></div>
    <div class="rail"><svg><use href="#i-eye"/></svg><svg><use href="#i-star"/></svg><svg><use href="#i-heart"/></svg><svg><use href="#i-cloud"/></svg></div></div></article>
  <article class="card"><div class="media" role="img" aria-label="Mother and daughter holding a gift by a Christmas tree" style="background:linear-gradient(135deg,#6b4a2a,#c8322e 55%,#e8d2b0)"></div>
    <div class="info"><div class="body"><div class="title"><span class="mark tweet"></span>Lorem Ipsum is simply dummy</div><p class="desc">Lorem Ipsum is simply dummy text of the printing and typesetting industry. Lorem Ipsum has been the industry's standard dummy text ever since.</p></div>
    <div class="rail"><svg><use href="#i-eye"/></svg><svg><use href="#i-star"/></svg><svg><use href="#i-heart"/></svg><svg><use href="#i-cloud"/></svg></div></div></article>
  <article class="card"><div class="media video" role="img" aria-label="Video player">
      <svg class="play" width="90" height="90" viewBox="0 0 90 90"><circle cx="45" cy="45" r="41" fill="none" stroke="#fff" stroke-width="5"/><path d="M36 28v34l27-17z" fill="#fff"/></svg>
      <div class="controls"><i class="dot"></i><i class="track"></i><i class="vol"></i></div></div>
    <div class="info"><div class="body"><div class="title"><span class="mark clip"></span>Lorem Ipsum is simply dummy</div><p class="desc">Lorem Ipsum is simply dummy text of the printing and typesetting industry. Lorem Ipsum has been the industry's standard dummy text ever since.</p></div>
    <div class="rail"><svg><use href="#i-eye"/></svg><svg><use href="#i-star"/></svg><svg><use href="#i-heart"/></svg><svg><use href="#i-cloud"/></svg></div></div></article>

  <!-- row 4 -->
  <article class="card"><div class="media" role="img" aria-label="Woman on the phone working at a laptop" style="background:linear-gradient(135deg,#8fbf5a,#f3f1ec 55%,#c9c9c9)"></div>
    <div class="info"><div class="body"><div class="title"><span class="mark post"></span>Lorem Ipsum is simply dummy</div><p class="desc">Lorem Ipsum is simply dummy text of the printing and typesetting industry. Lorem Ipsum has been the industry's standard dummy text ever since.</p></div>
    <div class="rail"><svg><use href="#i-eye"/></svg><svg><use href="#i-star"/></svg><svg><use href="#i-heart"/></svg><svg><use href="#i-cloud"/></svg></div></div></article>
  <article class="card"><div class="media" role="img" aria-label="Bright dining room with a wooden table" style="background:linear-gradient(180deg,#f1ead8,#b08a5a 60%,#5a3e24)"></div>
    <div class="info"><div class="body"><div class="title"><span class="mark tweet"></span>Lorem Ipsum is simply dummy</div><p class="desc">Lorem Ipsum is simply dummy text of the printing and typesetting industry. Lorem Ipsum has been the industry's standard dummy text ever since.</p></div>
    <div class="rail"><svg><use href="#i-eye"/></svg><svg><use href="#i-star"/></svg><svg><use href="#i-heart"/></svg><svg><use href="#i-cloud"/></svg></div></div></article>
  <article class="card"><div class="media" role="img" aria-label="Two children in winter clothes sitting in the snow" style="background:linear-gradient(135deg,#f4f4f6,#dcdde3 55%,#7a4a4a)"></div>
    <div class="info"><div class="body"><div class="title"><span class="mark clip"></span>Lorem Ipsum is simply dummy</div><p class="desc">Lorem Ipsum is simply dummy text of the printing and typesetting industry. Lorem Ipsum has been the industry's standard dummy text ever since.</p></div>
    <div class="rail"><svg><use href="#i-eye"/></svg><svg><use href="#i-star"/></svg><svg><use href="#i-heart"/></svg><svg><use href="#i-cloud"/></svg></div></div></article>

  <!-- row 5 -->
  <article class="card"><div class="media" role="img" aria-label="Family house under a blue sky" style="background:linear-gradient(180deg,#4f8fd6,#b7cde6 50%,#5f7a4a)"></div>
    <div class="info"><div class="body"><div class="title"><span class="mark post"></span>Lorem Ipsum is simply dummy</div><p class="desc">Lorem Ipsum is simply dummy text of the printing and typesetting industry. Lorem Ipsum has been the industry's standard dummy text ever since.</p></div>
    <div class="rail"><svg><use href="#i-eye"/></svg><svg><use href="#i-star"/></svg><svg><use href="#i-heart"/></svg><svg><use href="#i-cloud"/></svg></div></div></article>
  <article class="card"><div class="media" role="img" aria-label="Mother and baby in towels after a bath" style="background:linear-gradient(135deg,#f6f1ee,#e6c3b6 55%,#a6d6d2)"></div>
    <div class="info"><div class="body"><div class="title"><span class="mark tweet"></span>Lorem Ipsum is simply dummy</div><p class="desc">Lorem Ipsum is simply dummy text of the printing and typesetting industry. Lorem Ipsum has been the industry's standard dummy text ever since.</p></div>
    <div class="rail"><svg><use href="#i-eye"/></svg><svg><use href="#i-star"/></svg><svg><use href="#i-heart"/></svg><svg><use href="#i-cloud"/></svg></div></div></article>
  <article class="card"><div class="media video" role="img" aria-label="Video player">
      <svg class="play" width="90" height="90" viewBox="0 0 90 90"><circle cx="45" cy="45" r="41" fill="none" stroke="#fff" stroke-width="5"/><path d="M36 28v34l27-17z" fill="#fff"/></svg>
      <div class="controls"><i class="dot"></i><i class="track"></i><i class="vol"></i></div></div>
    <div class="info"><div class="body"><div class="title"><span class="mark clip"></span>Lorem Ipsum is simply dummy</div><p class="desc">Lorem Ipsum is simply dummy text of the printing and typesetting industry. Lorem Ipsum has been the industry's standard dummy text ever since.</p></div>
    <div class="rail"><svg><use href="#i-eye"/></svg><svg><use href="#i-star"/></svg><svg><use href="#i-heart"/></svg><svg><use href="#i-cloud"/></svg></div></div></article>

  <!-- row 6 -->
  <article class="card"><div class="media" role="img" aria-label="Dining room with a table and chairs" style="background:linear-gradient(135deg,#a9c9c4,#e8e2d4 50%,#5a3a24)"></div>
    <div class="info"><div class="body"><div class="title"><span class="mark post"></span>Lorem Ipsum is simply dummy</div><p class="desc">Lorem Ipsum is simply dummy text of the printing and typesetting industry. Lorem Ipsum has been the industry's standard dummy text ever since.</p></div>
    <div class="rail"><svg><use href="#i-eye"/></svg><svg><use href="#i-star"/></svg><svg><use href="#i-heart"/></svg><svg><use href="#i-cloud"/></svg></div></div></article>
  <article class="card"><div class="media" role="img" aria-label="Breakfast of cereal, milk, cheese and fruit" style="background:linear-gradient(135deg,#f3d35a,#9bc23a 45%,#f5f2ea 70%,#c0303a)"></div>
    <div class="info"><div class="body"><div class="title"><span class="mark tweet"></span>Lorem Ipsum is simply dummy</div><p class="desc">Lorem Ipsum is simply dummy text of the printing and typesetting industry. Lorem Ipsum has been the industry's standard dummy text ever since.</p></div>
    <div class="rail"><svg><use href="#i-eye"/></svg><svg><use href="#i-star"/></svg><svg><use href="#i-heart"/></svg><svg><use href="#i-cloud"/></svg></div></div></article>
  <article class="card"><div class="media" role="img" aria-label="Mother and daughter looking at a tablet" style="background:linear-gradient(135deg,#7fa96a,#e7d6c6 50%,#6a8fb8)"></div>
    <div class="info"><div class="body"><div class="title"><span class="mark clip"></span>Lorem Ipsum is simply dummy</div><p class="desc">Lorem Ipsum is simply dummy text of the printing and typesetting industry. Lorem Ipsum has been the industry's standard dummy text ever since.</p></div>
    <div class="rail"><svg><use href="#i-eye"/></svg><svg><use href="#i-star"/></svg><svg><use href="#i-heart"/></svg><svg><use href="#i-cloud"/></svg></div></div></article>

  <!-- row 7 -->
  <article class="card"><div class="media" role="img" aria-label="Woman relaxing on a green sofa" style="background:linear-gradient(135deg,#eef2e6,#a6c96a 55%,#6f9a3a)"></div>
    <div class="info"><div class="body"><div class="title"><span class="mark post"></span>Lorem Ipsum is simply dummy</div><p class="desc">Lorem Ipsum is simply dummy text of the printing and typesetting industry. Lorem Ipsum has been the industry's standard dummy text ever since.</p></div>
    <div class="rail"><svg><use href="#i-eye"/></svg><svg><use href="#i-star"/></svg><svg><use href="#i-heart"/></svg><svg><use href="#i-cloud"/></svg></div></div></article>
  <article class="card"><div class="media" role="img" aria-label="Woman working on a laptop in a bright room" style="background:linear-gradient(135deg,#f7f5ef,#e4d8c2 55%,#c9c9c9)"></div>
    <div class="info"><div class="body"><div class="title"><span class="mark tweet"></span>Lorem Ipsum is simply dummy</div><p class="desc">Lorem Ipsum is simply dummy text of the printing and typesetting industry. Lorem Ipsum has been the industry's standard dummy text ever since.</p></div>
    <div class="rail"><svg><use href="#i-eye"/></svg><svg><use href="#i-star"/></svg><svg><use href="#i-heart"/></svg><svg><use href="#i-cloud"/></svg></div></div></article>
  <article class="card"><div class="media video" role="img" aria-label="Video player">
      <svg class="play" width="90" height="90" viewBox="0 0 90 90"><circle cx="45" cy="45" r="41" fill="none" stroke="#fff" stroke-width="5"/><path d="M36 28v34l27-17z" fill="#fff"/></svg>
      <div class="controls"><i class="dot"></i><i class="track"></i><i class="vol"></i></div></div>
    <div class="info"><div class="body"><div class="title"><span class="mark clip"></span>Lorem Ipsum is simply dummy</div><p class="desc">Lorem Ipsum is simply dummy text of the printing and typesetting industry. Lorem Ipsum has been the industry's standard dummy text ever since.</p></div>
    <div class="rail"><svg><use href="#i-eye"/></svg><svg><use href="#i-star"/></svg><svg><use href="#i-heart"/></svg><svg><use href="#i-cloud"/></svg></div></div></article>
</main>

<div class="seal"></div>
<footer class="footer">Copyright © 2013 Quillo.me. All rights reserved.</footer>
</body>
</html>
```